Bright and vibrant Jewelry Designer Web Page

Hi creative artists,

My name is Marta, I'm a local jewelry designer with a small store in Duesseldorf Germany. All my Jewelrys are unique and hand crafted by my self.

My designs are colorful, young, modern and trendy as well as timeless and durable due to the high quality materials. I use gold, silver, jewelry, fresh water pearls and hand crafted glass.

Competitors are local goldsmith which produce custom-made jewelry.

I have started my business with my jewelry label "twigs and ribbons" 2007:
http://www.twigs-and-ribbons.de/start.php

In 2009 I have opened my store "Kupfer und Leinen" (silver and silk) together with a fashion designer:
http://www.kupfer-leinen.de/home.php
https://www.facebook.com/Kupfer.und.Leinen (latest jewelrys)

Scope of pages:
● welcome page
● category overview
- short introduction
- sub categories: Earring, Necklace, Ring, Bride Jewelry, ...
● category page
- short introduction
- products of this category
● product page
- short introduction
- about 3 to 4 pictures
- description: materials, dimensions
- price
- ! important ! related products
● contact page
- address
- contact form
● blog
- picture
- text

Conclusion:
● We need a emotional page
● Lots of impressive and brilliant product images
● A feminine touch
● Last but not least the design should reflect
- outstanding design
- uniqueness
- made-to-measure

Target Market(s)

Women in the mid 20's and 30's , interested in individual style, fashion and luxury goods

Industry/Entity Type

Jewelry

Requirements
Must have
• ● css for screen, mobile devices and print
● full function also with out JavaScript
● only use free available fonts e.g. Lumora Type Library (http://www.lumoratype.example/webfonts)
Should not have
• ● sound
● flash

```html
<!DOCTYPE html>
<html lang="en">
<head>
<meta charset="utf-8">
<title>Kupfer und Leinen – Jewelry Online Store</title>
<link href="https://fonts.googleapis.com/css2?family=Montserrat:wght@400;700&family=Open+Sans:wght@400;600&display=swap" rel="stylesheet">
<style>
:root{
  --ink:#3a2f2f;
  --muted:#9a9a9a;
  --faint:#c3c3c3;
  --rule:#cfcfcf;
  --brand:#8c5a66;
  --nav-top:#c2500f;
  --nav-bottom:#8a2806;
  --plum:#3e2526;
  --btn:#9c8686;
  --cart:#f7a21b;
  --card-border:#ececec;
  --circle:#d5d5d5;
}
*{box-sizing:border-box;margin:0;padding:0}
html,body{width:1024px;height:1200px;overflow:hidden;background:#fff}
body{position:relative;font-family:"Open Sans",Arial,sans-serif;color:var(--ink)}
a{color:inherit;text-decoration:none}
h2,h3,h4{font-weight:400}
.abs{position:absolute}

/* header */
.brand{left:66px;top:22px;font-family:"Montserrat",sans-serif;font-weight:400;font-size:42px;letter-spacing:1px;color:var(--brand);display:flex;align-items:center;gap:14px}
.brand-mark{width:22px;height:22px;border-radius:50%;background:var(--brand)}
.search{left:768px;top:64px;width:201px;height:18px;display:flex}
.search-field{flex:1;border:1px solid #e2e2e2;background:#fff}
.search-btn{width:45px;background:var(--plum);display:flex;align-items:center;justify-content:center}
.welcome{right:56px;top:92px;font-size:9.5px;color:var(--muted);letter-spacing:.3px;word-spacing:1px}
.welcome a{color:var(--ink)}
.header-rule{left:53px;top:124px;width:917px;height:1px;background:var(--rule)}
.phone{left:53px;top:139px;font-size:9.5px;letter-spacing:.5px;color:#555}
.toplinks{right:54px;top:142px;font-size:6.5px;text-transform:uppercase;letter-spacing:.5px;color:var(--faint);display:flex;gap:5px}
.toplinks .on{color:var(--ink)}
.toplinks .sep{color:#555}

/* nav */
.nav{left:53px;top:168px;width:917px;height:43px;background:linear-gradient(var(--nav-top),var(--nav-bottom));display:flex;align-items:center}
.nav-item{font-family:"Montserrat",sans-serif;font-size:10px;color:#fff;letter-spacing:.5px;padding:0 18px;border-right:1px solid rgba(255,255,255,.45);line-height:16px}
.cart{position:absolute;left:700px;top:13px;display:flex;align-items:center;font-family:"Montserrat",sans-serif;font-size:7px;font-weight:700;color:#2a1410;letter-spacing:.4px}
.cart-box{width:20px;height:17px;background:var(--cart);margin-right:13px}
.cart .cur{color:#fff;font-weight:400;letter-spacing:9px;font-size:8px;margin-left:14px}

/* slider */
.hero{left:53px;top:227px;width:604px;height:272px;overflow:hidden;
  background:linear-gradient(100deg,#b9b9bd 0%,#e6e6e8 28%,#f6f3ec 48%,#e2cf9f 62%,#d9d6d2 78%,#c4c4c8 100%)}
.hero-caption{left:0;bottom:0;width:300px;height:74px;background:rgba(120,110,112,.55);padding:10px 0 0 19px;font-family:"Montserrat",sans-serif;font-weight:700;color:#fff;line-height:1}
.hero-caption .big{font-size:26px;letter-spacing:1px}
.hero-caption .sub{font-size:20px;margin-top:4px;letter-spacing:.6px}
.dots{left:545px;top:250px;display:flex;gap:3px}
.dot{width:11px;height:11px;border-radius:50%;background:#fff}
.dot.on{background:#222}
.side-banner{left:679px;top:227px;width:290px;height:272px;overflow:hidden;
  background:linear-gradient(160deg,#1a1612 0%,#2a2116 30%,#8a6a2e 50%,#2a2116 66%,#070707 100%)}
.side-caption{left:27px;top:224px;font-family:"Montserrat",sans-serif;font-weight:700;color:#fff;font-size:17px;line-height:16px;letter-spacing:.3px}
.side-caption small{font-size:11px}

/* featured */
.section-bar{left:53px;top:517px;width:917px;height:34px;background:var(--plum);color:#fff;font-family:"Montserrat",sans-serif;font-size:9.5px;letter-spacing:.6px;padding:11px 0 0 27px}
.card{top:556px;width:224px;height:287px;border:1px solid var(--card-border);background:#fcfcfc}
.card-title{position:absolute;left:21px;top:15px;font-size:10px;color:#222;letter-spacing:.4px}
.card-img{position:absolute;left:32px;top:55px;width:160px;height:120px;border-radius:4px}
.card-desc{position:absolute;left:21px;top:195px;width:178px;font-size:8px;line-height:11.5px;color:var(--faint);letter-spacing:.2px}
.card-buy{position:absolute;left:21px;top:246px;display:flex;align-items:center;gap:8px}
.btn{background:var(--btn);color:#fff;font-size:8px;width:72px;height:23px;display:flex;align-items:center;justify-content:center;letter-spacing:.4px}
.price{font-family:"Montserrat",sans-serif;font-size:17px;color:#222;letter-spacing:.6px}

.dotted{left:53px;width:917px;border-top:2px dotted #d0d0d0}

/* promos */
.promo{top:896px;width:294px;height:128px}
.promo-caption{position:absolute;left:13px;bottom:5px;font-family:"Montserrat",sans-serif;color:#fff;line-height:1}
.promo-caption .l1{font-size:17px;letter-spacing:.3px}
.promo-caption .l2{font-size:22px;font-weight:700;letter-spacing:.5px}
.promo-caption .l3{font-size:12px;letter-spacing:.6px}

/* footer */
.foot-col{top:1073px}
.foot-col h4{font-family:"Montserrat",sans-serif;font-size:9.5px;letter-spacing:.5px;color:#333;margin-bottom:18px}
.foot-col li{list-style:none;font-size:8px;color:var(--muted);letter-spacing:.4px;height:21.5px;padding-left:11px;position:relative}
.foot-col li::before{content:"";position:absolute;left:0;top:4px;border-left:4px solid #444;border-top:2.5px solid transparent;border-bottom:2.5px solid transparent}
.copyright{left:777px;top:1112px;font-family:"Montserrat",sans-serif;font-weight:700;font-size:7px;letter-spacing:.6px;color:#222}
.social{left:776px;top:1151px;display:flex;gap:5px}
.social span{width:29px;height:25px;border-radius:50%;background:var(--circle)}
</style>
</head>
<body>

<header>
  <a class="abs brand" href="#"><span>Kupfer und Leinen</span><span class="brand-mark"></span></a>
  <form class="abs search">
    <span class="search-field"></span>
    <span class="search-btn"><svg width="9" height="9" viewBox="0 0 10 10"><circle cx="4" cy="4" r="3" fill="none" stroke="#fff" stroke-width="1.3"/><line x1="6.2" y1="6.2" x2="9" y2="9" stroke="#fff" stroke-width="1.5"/></svg></span>
  </form>
  <p class="abs welcome">Welcome visitor you can <a href="#">Login</a> or <a href="#">Create an account</a></p>
  <div class="abs header-rule"></div>
  <p class="abs phone">Telephone: 1(234) 555-0190</p>
  <nav class="abs toplinks">
    <a class="on" href="#">Home</a><span class="sep">•</span>
    <a href="#">Wish list(0)</a><span class="sep">•</span>
    <a href="#">My account</a><span class="sep">•</span>
    <a href="#">Shopping cart</a><span class="sep">•</span>
    <a href="#">Checkout</a>
  </nav>
  <nav class="abs nav">
    <a class="nav-item" href="#">WEDDING</a>
    <a class="nav-item" href="#">RINGS</a>
    <a class="nav-item" href="#">NECKLACES</a>
    <a class="nav-item" href="#">EARRINGS</a>
    <a class="nav-item" href="#">BRACELETS</a>
    <a class="nav-item" href="#">WATCHES</a>
    <div class="cart"><span class="cart-box"></span><span>CART: &nbsp;0 ITEM(S) - $0.00 ⌄</span><span class="cur">€£$</span></div>
  </nav>
</header>

<main>
  <section class="abs hero" role="img" aria-label="Gold bracelets and rings arranged on a clear glass cube">
    <div class="abs hero-caption"><div class="big">SALE</div><div class="sub">UP TO 40% OFF</div></div>
    <div class="abs dots"><span class="dot on"></span><span class="dot"></span></div>
  </section>
  <section class="abs side-banner" role="img" aria-label="Layered gold collar necklace with teardrop pendant on black velvet">
    <p class="abs side-caption">VARELA <small>COLLECTIONS</small><br>ONLY EXCLUSIVES</p>
  </section>

  <h2 class="abs section-bar">FEATURED PRODUCTS</h2>

  <article class="abs card" style="left:53px">
    <h3 class="card-title">Adipiscing elit, sed diam...</h3>
    <div class="card-img" role="img" aria-label="Gold ring with a large amber gemstone" style="background:linear-gradient(135deg,#f3dcb0 0%,#d99a3e 45%,#a8662a 70%,#eed2a4 100%)"></div>
    <p class="card-desc">Precious metals have always been a detector of prosperity and high social rank. Just re...</p>
    <div class="card-buy"><a class="btn" href="#">Add to cart</a><span class="price">$225.25</span></div>
  </article>
  <article class="abs card" style="left:284px">
    <h3 class="card-title">Magna aliqua....</h3>
    <div class="card-img" role="img" aria-label="Wide band ring set with rows of rubies and diamonds" style="background:linear-gradient(135deg,#ecc6cf 0%,#b3173f 45%,#7e0f2c 70%,#e6bcc6 100%)"></div>
    <p class="card-desc">Precious metals have always been a detector of prosperity and high social rank. Just re...</p>
    <div class="card-buy"><a class="btn" href="#">Add to cart</a><span class="price">$119.50</span></div>
  </article>
  <article class="abs card" style="left:516px">
    <h3 class="card-title">Lorem ipsum dolor sit...</h3>
    <div class="card-img" role="img" aria-label="Gold link bracelet with small red stones" style="background:linear-gradient(135deg,#f6e6c0 0%,#ddb25a 45%,#b9853a 70%,#f1ddb2 100%)"></div>
    <p class="card-desc">Precious metals have always been a detector of prosperity and high social rank. Just re...</p>
    <div class="card-buy"><a class="btn" href="#">Add to cart</a><span class="price">$107.75</span></div>
  </article>
  <article class="abs card" style="left:747px">
    <h3 class="card-title">Exerci tation ullamcorper...</h3>
    <div class="card-img" role="img" aria-label="Emerald jewelry set with pendant, earrings and ring" style="background:linear-gradient(135deg,#d3ead2 0%,#3e9a4a 45%,#c9b67a 72%,#e8efe0 100%)"></div>
    <p class="card-desc">Precious metals have always been a detector of prosperity and high social rank. Just re...</p>
    <div class="card-buy"><a class="btn" href="#">Add to cart</a><span class="price">$96.00</span></div>
  </article>

  <div class="abs dotted" style="top:870px"></div>

  <a class="abs promo" href="#" style="left:56px;background:linear-gradient(90deg,#2a2222,#5a4640 50%,#1c1818)" role="img" aria-label="Model presenting silver jewelry in her hand">
    <span class="promo-caption"><span class="l1">FREE SHIPPING</span><br><span class="l2">ON ORDERS</span><br><span class="l3">OVER $ 400.00</span></span>
  </a>
  <a class="abs promo" href="#" style="left:367px;background:linear-gradient(120deg,#2a2a2a,#6a6a6a 55%,#1e1e1e)" role="img" aria-label="Silver diamond bracelet on dark fabric">
    <span class="promo-caption"><span class="l1">GET EXCLUSIVE</span><br><span class="l2">DISCOUNT</span><br><span class="l3">ON ALL COLLECTIONS</span></span>
  </a>
  <a class="abs promo" href="#" style="left:678px;background:linear-gradient(90deg,#d6b98e,#b98258 55%,#e4cfa8)" role="img" aria-label="Woman in summer light wearing gold bangles">
    <span class="promo-caption"><span class="l1" style="font-size:22px">2013</span><br><span class="l2">SUMMER</span><br><span class="l3">WOMEN'S COLLECTION</span></span>
  </a>

  <div class="abs dotted" style="top:1048px"></div>
</main>

<footer>
  <div class="abs foot-col" style="left:56px"><h4>INFORMATION</h4><ul><li>About</li><li>Delivery</li><li>Privacy Policy</li><li>Terms &amp; Conditions</li></ul></div>
  <div class="abs foot-col" style="left:199px"><h4>CUSTOMER SERVICE</h4><ul><li>Contact Us</li><li>Returns</li><li>Site Map</li></ul></div>
  <div class="abs foot-col" style="left:342px"><h4>EXTRAS</h4><ul><li>Brands</li><li>Gift Vouchers</li><li>Affiliates</li><li>Specials</li></ul></div>
  <div class="abs foot-col" style="left:486px"><h4>MY ACCOUNT</h4><ul><li>My Account</li><li>Order History</li><li>Wish List</li><li>Newsletter</li></ul></div>
  <p class="abs copyright">JEWELRY ONLINE STORE © 2013</p>
  <div class="abs social" aria-label="Social links"><span></span><span></span><span></span><span></span></div>
</footer>

</body>
</html>
```